Prestige Car Bodyshop Business Card

We are a car bodyshop based in the UK. Our customer base is mainly prestige high-value vehicles. I am looking for a classy and stylish business card design for my staff to give out to customers, with their direct email and phone number, as well as our main email and phone number with address details

I am also looking to have a general business card design with just our main company address and contact details, but also have a space to add a manufacturer approval logo (i.e Velmora, Orek, Tovalo etc... logo) in the corner somewhere.

I do not particularly want any outlines or pictures of cars on the card, I would just like a quality high-end look.

Please feel free to get in touch if you have any questions or queries?

Many Thanks

Malcolm

Target Market(s)

Prestige vehicle owners

Industry/Entity Type

Automotive

Contact Information for Business Card

I am looking for a classy and stylish business card design for my staff to give out to customers, with their direct email and phone number, as well as our main email and phone number with address details

Font styles to use
Sans Serif

Colors

Designer to choose colors to be used in the design.

Requirements
Nice to have
• I do not particularly want any outlines or pictures of cars on the card, I would just like a quality high-end look.

```html
<!DOCTYPE html>
<html lang="en">
<head>
<meta charset="utf-8">
<title>Hartwell Accident Repair Centre – Business Cards</title>
<link rel="stylesheet" href="https://fonts.googleapis.com/css2?family=Source+Sans+3:wght@300;400;600&display=swap">
<style>
  :root {
    --stage: #2a2a2a;
    --card-dark: #262626;
    --card-light: #f3f3f4;
    --brand-blue: #1f5fa6;
    --brand-orange: #d9822b;
    --ink-navy: #2c3f6b;
    --ink-grey: #4a4a4a;
  }
  * { margin: 0; padding: 0; box-sizing: border-box; }
  html, body { width: 1200px; height: 716px; overflow: hidden; }
  body {
    background: var(--stage);
    font-family: "Source Sans 3", sans-serif;
    position: relative;
  }
  .card {
    position: absolute;
    top: 208px;
    width: 520px;
    height: 300px;
    border-radius: 3px;
    box-shadow: 0 10px 30px rgba(0,0,0,0.45);
    overflow: hidden;
  }
  .card--front { left: 50px; background: var(--card-dark); }
  .card--back  { left: 630px; background: var(--card-light); }

  .brand {
    position: absolute;
    display: flex;
    align-items: flex-end;
  }
  .brand__dot { border-radius: 50%; background: var(--brand-blue); flex: none; }
  .brand__text { display: flex; flex-direction: column; white-space: nowrap; }
  .brand__name {
    font-weight: 300;
    text-transform: uppercase;
    line-height: 1;
  }
  .brand__rule { height: 2px; margin: 4px 0 3px; }
  .brand__tagline {
    font-weight: 400;
    text-transform: uppercase;
    line-height: 1.1;
  }

  .card--front .brand { left: 86px; top: 92px; gap: 14px; }
  .card--front .brand__dot { width: 90px; height: 90px; margin-bottom: 24px; }
  .card--front .brand__name { color: var(--brand-orange); font-size: 44px; letter-spacing: 1px; }
  .card--front .brand__rule { background: var(--brand-orange); width: 220px; }
  .card--front .brand__tagline { color: var(--brand-orange); font-size: 15px; letter-spacing: 1px; }

  .card--back .brand { left: 30px; top: 92px; gap: 8px; }
  .card--back .brand__dot { width: 62px; height: 62px; margin-bottom: 18px; }
  .card--back .brand__name { color: var(--ink-navy); font-size: 27px; letter-spacing: 0.5px; }
  .card--back .brand__rule { background: var(--ink-navy); width: 148px; height: 1.5px; }
  .card--back .brand__tagline { color: var(--ink-navy); font-size: 10px; letter-spacing: 0.4px; }

  .divider {
    position: absolute;
    left: 262px; top: 70px;
    width: 1.5px; height: 160px;
    background: var(--ink-navy);
  }
  .contact {
    position: absolute;
    left: 284px; top: 76px;
    width: 220px;
    color: var(--ink-grey);
  }
  .contact__name { font-size: 21px; font-weight: 600; color: #555; line-height: 1.1; }
  .contact__title { font-size: 14px; margin-bottom: 16px; }
  .contact__row {
    display: flex; align-items: flex-start; gap: 8px;
    font-size: 14px; line-height: 1.3; margin-bottom: 9px;
  }
  .contact__row svg { width: 13px; height: 13px; flex: none; margin-top: 2px; fill: var(--ink-navy); }
</style>
</head>
<body>

<section class="card card--front" aria-label="Business card front">
  <div class="brand">
    <div class="brand__dot"></div>
    <div class="brand__text">
      <span class="brand__name">Hartwell</span>
      <span class="brand__rule"></span>
      <span class="brand__tagline">Accident Repair Centre</span>
    </div>
  </div>
</section>

<section class="card card--back" aria-label="Business card back">
  <div class="brand">
    <div class="brand__dot"></div>
    <div class="brand__text">
      <span class="brand__name">Hartwell</span>
      <span class="brand__rule"></span>
      <span class="brand__tagline">Accident Repair Centre</span>
    </div>
  </div>

  <div class="divider"></div>

  <div class="contact">
    <p class="contact__name">Your Name</p>
    <p class="contact__title">Job title</p>
    <p class="contact__row">
      <svg viewBox="0 0 16 16" aria-hidden="true"><path d="M3 2h3l1.5 3.5-2 1.3a8 8 0 0 0 3.7 3.7l1.3-2L14 10v3a1 1 0 0 1-1 1A11 11 0 0 1 2 3a1 1 0 0 1 1-1z"/></svg>
      <span>000 000 0000</span>
    </p>
    <p class="contact__row">
      <svg viewBox="0 0 16 16" aria-hidden="true"><path d="M1 3h14v10H1z M2 4l6 5 6-5" fill="none" stroke="#2c3f6b" stroke-width="1.4"/></svg>
      <span>youremail@xyz.com</span>
    </p>
    <p class="contact__row">
      <svg viewBox="0 0 16 16" aria-hidden="true"><path d="M8 1a5 5 0 0 1 5 5c0 4-5 9-5 9S3 10 3 6a5 5 0 0 1 5-5zm0 3a2 2 0 1 0 0 4 2 2 0 0 0 0-4z"/></svg>
      <span>0000, Any street, Anywhere<br>Province name 00000</span>
    </p>
  </div>
</section>

</body>
</html>
```